Jewelry Wholesale Business Card Design

Company name: VORELLA
Business Background: Wholesale jewelry store located in downtown Los Angeles. We specialize in 18k gold-filled, stainless steel, 14kt gold, and natural stone jewelry.
website: www.vorella-example.com
Instagram: vorella_
Email: sales@vorella-example.com
Address: 318 W. BIRCH AVE #27, #109
LOS ANGELES, CA 90087
(213)555-0147

We would like to create a simple, yet elegant business card for my store
-Includes company logo
-Black background preferred
-Gold metallic color letters
- Lists the type of products we sell
-Small icons for instagram handle, phone, email, and website

Target Market(s)

Hispanic community, age 12-40

Industry/Entity Type

Jewelry Wholesale

Contact Information for Business Card

logo, business location, website, phone number, email, instagram, lists type of products, Dylan Moret(my name)

Font styles to use
Serif
Sans Serif

Colors
FFF300
FFF600
FEFA6F
FFFEC7
FFFEE8

Requirements
Must have
• logo, business location, website, phone number, email, instagram, lists type of products, Dylan Moret(my name)

```html
<!DOCTYPE html>
<html lang="en">
<head>
<meta charset="utf-8">
<title>VORELLA Business Card</title>
<link href="https://fonts.googleapis.com/css2?family=Montserrat:wght@400;500;600;700&display=swap" rel="stylesheet">
<style>
  :root{
    --backdrop:#303030;
    --card:#121212;
    --gold:#d6b160;
    --gold-edge:#b8954a;
  }
  *{margin:0;padding:0;box-sizing:border-box}
  html,body{width:1200px;height:801px;overflow:hidden;background:var(--backdrop)}
  body{position:relative;font-family:"Montserrat",sans-serif;color:var(--gold)}
  .card{
    position:absolute;top:246px;width:540px;height:309px;
    background:var(--card);border:1.5px solid var(--gold-edge);
  }
  .card--front{left:40px}
  .card--back{left:620px}

  /* front */
  .brand{
    position:absolute;left:0;width:300px;top:62px;
    display:flex;align-items:center;justify-content:center;gap:12px;
  }
  .brand__dot{width:10px;height:10px;border-radius:50%;background:var(--gold)}
  .brand__name{font-weight:600;font-size:40px;letter-spacing:3px}
  .address{
    position:absolute;left:0;width:300px;top:166px;text-align:center;
    font-size:13px;line-height:20px;letter-spacing:.4px;
  }
  .address__person{font-weight:700;font-size:13px;letter-spacing:1px}
  .address__company{font-weight:600;font-size:12px;letter-spacing:1px;margin-bottom:4px}
  .divider{position:absolute;left:312px;top:150px;width:1px;height:70px;background:var(--gold)}
  .contacts{position:absolute;left:330px;top:148px;list-style:none;font-size:12.5px;line-height:19px}
  .contacts li{display:flex;align-items:center;gap:7px;white-space:nowrap}
  .contacts svg{width:11px;height:11px;flex:none}
  .contacts .at{width:11px;text-align:center;font-weight:600;font-size:11px}

  /* back */
  .monogram{
    position:absolute;left:0;right:0;top:110px;text-align:center;
    font-weight:600;font-size:34px;letter-spacing:4px;
  }
  .products{
    position:absolute;left:0;right:0;bottom:40px;text-align:center;
    font-size:13px;letter-spacing:.2px;white-space:nowrap;
  }
  .products .sep{margin:0 6px;font-size:8px;vertical-align:middle}
</style>
</head>
<body>

<section class="card card--front">
  <div class="brand"><span class="brand__dot"></span><span class="brand__name">VORELLA</span></div>
  <div class="address">
    <p class="address__person">DYLAN MORET</p>
    <p class="address__company">VORELLA</p>
    <p>318 W. BIRCH AVE #27, #109</p>
    <p>LOS ANGELES, CA 90087</p>
  </div>
  <div class="divider"></div>
  <ul class="contacts">
    <li><svg viewBox="0 0 12 12"><path fill="var(--gold)" d="M2.5 1l2 2.2-1 1.3a6 6 0 0 0 4 4l1.3-1 2.2 2-1.2 1.5C5.3 11 1 6.7.9 2.2z"/></svg>(213)555-0147</li>
    <li><svg viewBox="0 0 12 12"><rect x="0.5" y="2.5" width="11" height="7.5" fill="var(--gold)"/><path d="M1 3l5 3.8L11 3" stroke="var(--card)" fill="none"/></svg>sales@vorella-example.com</li>
    <li><svg viewBox="0 0 12 12"><circle cx="6" cy="6" r="5" fill="none" stroke="var(--gold)" stroke-width="1.2"/><path d="M1 6h10M6 1c-2.5 3-2.5 7 0 10M6 1c2.5 3 2.5 7 0 10" stroke="var(--gold)" fill="none" stroke-width=".9"/></svg>www.vorella-example.com</li>
    <li><span class="at">@</span>vorella_</li>
  </ul>
</section>

<section class="card card--back">
  <div class="monogram">VORELLA</div>
  <p class="products">18k gold-filled<span class="sep">●</span>stainless steel<span class="sep">●</span>14kt gold<span class="sep">●</span>and natural stone jewelry</p>
</section>

</body>
</html>
```